SEO AND WEB DESIGN COMPANY BUSINESS CARD DESIGN

I need an eye catching , simple business card design that will match my logo . I need 2 versions of it ( white background and black background) - SOME PEOPLE DID NOT GET IT AND SENDING US FRONT WHITE BACK WHITE VERSIONS WHICH IS NOT CORRECT.

ONE VERSION SHOULD BE BACK AND FRONT ALL BLACK , SECOND VERSION SHOULD BE BACK AND FRONT ALL WHITE

logo psd files are attached for both versions. The business card is going to have : First Name- Last name - position - phone numbers

```html
<!DOCTYPE html>
<html lang="en">
<head>
<meta charset="utf-8">
<title>Norvelle Business Cards</title>
<link href="https://fonts.googleapis.com/css2?family=Source+Sans+3:wght@400;600;700&display=swap" rel="stylesheet">
<style>
  :root {
    --bg: #e4e4e4;
    --card-dark: #2e2f31;
    --card-light: #f4f4f4;
    --ink-dark: #111111;
    --ink-light: #ffffff;
    --accent: #4f86c6;
    --shadow: rgba(0,0,0,0.35);
  }
  * { margin: 0; padding: 0; box-sizing: border-box; }
  html, body { width: 1200px; height: 960px; overflow: hidden; }
  body {
    background: var(--bg);
    font-family: "Source Sans 3", sans-serif;
    position: relative;
  }
  .card {
    position: absolute;
    width: 500px;
    height: 286px;
    box-shadow: 2px 3px 5px var(--shadow);
  }
  .card--dark { background: var(--card-dark); color: var(--ink-light); }
  .card--light { background: var(--card-light); color: var(--ink-dark); }
  .card--front-dark { left: 72px; top: 166px; }
  .card--front-light { left: 622px; top: 166px; }
  .card--back-dark { left: 72px; top: 495px; }
  .card--back-light { left: 624px; top: 495px; }

  .brand {
    position: absolute;
    left: 0; right: 0;
    display: flex;
    align-items: center;
    justify-content: center;
    gap: 12px;
  }
  .brand__dot {
    border-radius: 50%;
    background: var(--accent);
  }
  .brand__name {
    font-weight: 700;
    letter-spacing: 1px;
    line-height: 1;
  }
  .card--dark .brand__name { color: var(--ink-light); }
  .card--light .brand__name { color: var(--ink-dark); }

  .brand--front { top: 108px; }
  .brand--front .brand__dot { width: 30px; height: 30px; }
  .brand--front .brand__name { font-size: 56px; }

  .brand--back { top: 62px; }
  .brand--back .brand__dot { width: 22px; height: 22px; }
  .brand--back .brand__name { font-size: 40px; }

  .person {
    position: absolute;
    right: 272px;
    top: 182px;
    text-align: right;
  }
  .person__name {
    color: var(--accent);
    font-size: 17px;
    font-weight: 600;
    line-height: 1.1;
  }
  .person__role { font-size: 13px; line-height: 1.3; }

  .divider {
    position: absolute;
    left: 250px;
    top: 160px;
    width: 1px;
    height: 89px;
  }
  .card--dark .divider { background: var(--ink-light); }
  .card--light .divider { background: var(--ink-dark); }

  .contact {
    position: absolute;
    left: 268px;
    top: 161px;
    font-size: 13px;
    line-height: 17px;
  }
  .contact__address { margin-bottom: 7px; }
  .contact__row { display: flex; align-items: center; gap: 4px; }
  .contact__row svg { width: 11px; height: 11px; flex: none; }
</style>
</head>
<body>

  <section class="card card--dark card--front-dark">
    <div class="brand brand--front">
      <span class="brand__dot"></span>
      <span class="brand__name">NORVELLE</span>
    </div>
  </section>

  <section class="card card--light card--front-light">
    <div class="brand brand--front">
      <span class="brand__dot"></span>
      <span class="brand__name">NORVELLE</span>
    </div>
  </section>

  <section class="card card--dark card--back-dark">
    <div class="brand brand--back">
      <span class="brand__dot"></span>
      <span class="brand__name">NORVELLE</span>
    </div>
    <div class="person">
      <p class="person__name">Daniel Carver</p>
      <p class="person__role">President</p>
    </div>
    <div class="divider"></div>
    <div class="contact">
      <p class="contact__address">#310 2480 Harbor St<br>Kelwood BC V2K 4R8</p>
      <p class="contact__row">
        <svg viewBox="0 0 12 12"><path d="M2.5 1 L4.5 1 L5.3 3.5 L4 4.5 Q5 7 7.5 8 L8.5 6.7 L11 7.5 L11 9.5 Q10.5 11 9 11 Q1 10 1 3 Q1 1.5 2.5 1Z" fill="#4f86c6"/></svg>
        (555) 014- 2286
      </p>
      <p class="contact__row">
        <svg viewBox="0 0 12 12"><rect x="1" y="2.5" width="10" height="7" fill="none" stroke="#4f86c6" stroke-width="1.2"/><path d="M1 2.5 L6 6.5 L11 2.5" fill="none" stroke="#4f86c6" stroke-width="1.2"/></svg>
        daniel@norvelledm.ca
      </p>
      <p class="contact__row">
        <svg viewBox="0 0 12 12"><circle cx="6" cy="6" r="5" fill="none" stroke="#4f86c6" stroke-width="1"/><ellipse cx="6" cy="6" rx="2.2" ry="5" fill="none" stroke="#4f86c6" stroke-width="1"/><path d="M1 6 H11" stroke="#4f86c6" stroke-width="1"/></svg>
        www.norvelledm.ca
      </p>
    </div>
  </section>

  <section class="card card--light card--back-light">
    <div class="brand brand--back">
      <span class="brand__dot"></span>
      <span class="brand__name">NORVELLE</span>
    </div>
    <div class="person">
      <p class="person__name">Daniel Carver</p>
      <p class="person__role">President</p>
    </div>
    <div class="divider"></div>
    <div class="contact">
      <p class="contact__address">#310 2480 Harbor St<br>Kelwood BC V2K 4R8</p>
      <p class="contact__row">
        <svg viewBox="0 0 12 12"><path d="M2.5 1 L4.5 1 L5.3 3.5 L4 4.5 Q5 7 7.5 8 L8.5 6.7 L11 7.5 L11 9.5 Q10.5 11 9 11 Q1 10 1 3 Q1 1.5 2.5 1Z" fill="#4f86c6"/></svg>
        (555) 014- 2286
      </p>
      <p class="contact__row">
        <svg viewBox="0 0 12 12"><rect x="1" y="2.5" width="10" height="7" fill="none" stroke="#4f86c6" stroke-width="1.2"/><path d="M1 2.5 L6 6.5 L11 2.5" fill="none" stroke="#4f86c6" stroke-width="1.2"/></svg>
        daniel@norvelledm.ca
      </p>
      <p class="contact__row">
        <svg viewBox="0 0 12 12"><circle cx="6" cy="6" r="5" fill="none" stroke="#4f86c6" stroke-width="1"/><ellipse cx="6" cy="6" rx="2.2" ry="5" fill="none" stroke="#4f86c6" stroke-width="1"/><path d="M1 6 H11" stroke="#4f86c6" stroke-width="1"/></svg>
        www.norvelledm.ca
      </p>
    </div>
  </section>

</body>
</html>
```